Tarrow Building Performance

Id like for my business card to be very bold and professional. Incorporating the business logo, the main services offered, and my contact info. Services are spray foam, insulation, new construction, retrofit, weatherization.

When opening this project sketch harbor was not able to upload my new logo that I picked from another recent sketch harbor project. Does anyone know how i could upload my logo onto the page for design of the business cards?

Target Market(s)

Building owners, contractors

Industry/Entity Type

Building Insulation and performance improvements

Contact Information for Business Card

Owner, Email dean@tarrowbuildingperformance.example Phone number 555-208-6147

Colors
0054AA
0677BA
7BADD7
CADEEF
E8F1F8
F0912C
F2A743
F7CA91
FBE8D2
FDF5EE

Requirements
Must have
• Services- spray foam, cellulose, mineral wool, fiberglass, air sealing, new construction, retrofit, weatherization, energy saving assesments

```html
<!DOCTYPE html>
<html lang="en">
<head>
<meta charset="utf-8">
<title>Tarrow Building Performance – Business Card</title>
<link href="https://fonts.googleapis.com/css2?family=Montserrat:wght@400;500;700;800&family=Roboto+Condensed:wght@400&display=swap" rel="stylesheet">
<style>
  :root {
    --backdrop: #9a9a9a;
    --card-navy: #0b1633;
    --accent-blue: #35b4e6;
    --accent-orange: #f0802a;
    --text-light: #e8f1f8;
  }
  * { margin: 0; padding: 0; box-sizing: border-box; }
  html, body { width: 1200px; height: 1108px; overflow: hidden; }
  body {
    background: var(--backdrop);
    position: relative;
    font-family: "Montserrat", sans-serif;
  }
  .card {
    position: absolute;
    left: 240px;
    width: 718px;
    height: 411px;
    background: var(--card-navy);
    border-radius: 30px;
    border-left: 3px solid var(--accent-blue);
    border-bottom: 3px solid var(--accent-blue);
    overflow: hidden;
  }
  .card-front { top: 119px; }
  .card-back { top: 581px; }

  .brand {
    position: absolute;
    display: flex;
    align-items: center;
    color: var(--accent-orange);
    font-family: "Montserrat", sans-serif;
    font-weight: 800;
    text-transform: uppercase;
    line-height: 1.05;
  }
  .brand-mark {
    flex: none;
    background: var(--accent-blue);
  }
  .brand-front {
    left: 72px; top: 118px;
    font-size: 52px;
    gap: 24px;
  }
  .brand-front .brand-mark { width: 40px; height: 40px; }
  .brand-front .brand-sub { font-size: 28px; letter-spacing: 0.5px; }

  .brand-back {
    left: 34px; top: 34px;
    font-size: 33px;
    gap: 14px;
  }
  .brand-back .brand-mark { width: 24px; height: 24px; }
  .brand-back .brand-sub { font-size: 17.5px; letter-spacing: 0.3px; }

  .holder {
    position: absolute;
    left: 33px; top: 231px;
  }
  .holder-name {
    color: var(--accent-orange);
    font-weight: 700;
    font-size: 30px;
    line-height: 1.1;
  }
  .holder-role {
    color: var(--text-light);
    font-weight: 400;
    font-size: 18px;
    letter-spacing: 0.6px;
    margin-top: 6px;
  }

  .contact {
    position: absolute;
    left: 33px; top: 326px;
    list-style: none;
    font-family: "Roboto Condensed", sans-serif;
    color: var(--text-light);
    font-size: 17px;
  }
  .contact li {
    display: flex;
    align-items: center;
    gap: 9px;
    height: 28px;
  }
  .contact svg { width: 16px; height: 14px; fill: var(--accent-blue); }

  .services {
    position: absolute;
    right: 29px; top: 76px;
    text-align: right;
  }
  .services-title {
    color: var(--accent-blue);
    font-weight: 700;
    font-size: 34px;
    line-height: 1;
    margin-bottom: 14px;
  }
  .services-list { list-style: none; }
  .services-list li {
    color: var(--text-light);
    font-size: 17.5px;
    letter-spacing: 0.6px;
    height: 28.5px;
    display: flex;
    justify-content: flex-end;
    align-items: center;
    gap: 5px;
  }
  .services-list li::after {
    content: "";
    width: 8px; height: 8px;
    border-radius: 50%;
    background: var(--accent-blue);
    margin-top: 4px;
  }
</style>
</head>
<body>

<section class="card card-front" aria-label="Business card front">
  <div class="brand brand-front">
    <span class="brand-mark"></span>
    <div>
      <div class="brand-name">Tarrow</div>
      <div class="brand-sub">Building Performance</div>
    </div>
  </div>
</section>

<section class="card card-back" aria-label="Business card back">
  <div class="brand brand-back">
    <span class="brand-mark"></span>
    <div>
      <div class="brand-name">Tarrow</div>
      <div class="brand-sub">Building Performance</div>
    </div>
  </div>

  <div class="holder">
    <div class="holder-name">Dean Marlow</div>
    <div class="holder-role">Owner</div>
  </div>

  <ul class="contact">
    <li>
      <svg viewBox="0 0 16 14" aria-hidden="true"><path d="M1 5c0-2 3-3.5 7-3.5S15 3 15 5v1.5h-3.5V4.5h-7v2H1z"/><path d="M3 7.5h10l1.5 5.5h-13z"/></svg>
      <span>555-208-6147</span>
    </li>
    <li>
      <svg viewBox="0 0 16 14" aria-hidden="true"><path d="M0 2h16v10H0z M1.5 3.2 8 8l6.5-4.8v-.2h-13z" fill-rule="evenodd"/></svg>
      <span>dean@tarrowbuildingperformance.example</span>
    </li>
  </ul>

  <div class="services">
    <h2 class="services-title">Services</h2>
    <ul class="services-list">
      <li>Spray foam</li>
      <li>Cellulose</li>
      <li>Mineral wool</li>
      <li>Fiberglass</li>
      <li>Air sealing</li>
      <li>New construction</li>
      <li>Retrofit</li>
      <li>Weatherization</li>
      <li>Energy saving assesments</li>
    </ul>
  </div>
</section>

</body>
</html>
```